Designs for a fundrasining event a Brown Tie Beer and Wine event

We need a flyer, brochure, and tickets for entry for a brown tie event that will be a beer and wine pairing fundraising event to be held on May 9th from 6pm to 10pm at the Maplecrest Restaurant in Cedar Lake, Indiana, USA. There will be approximately 10 silent auction items and 5 or so sponsors that we will want to have the logos of the sponsors on what we can as well, attached are the logo for Open Hearth Foundation, IV NFP, which is the nonprofit hosting the event, there is also a logo for Dunmore Law, LLC which is one of the sponsors (this is so you have an idea of the other 4 or so that we would also want incorporated somehow). Please ask as many questions as you may have to clarify.

Industry/Entity Type

Event

Contact Information for Business Card

Open Hearth
Wendy P. Halvorsen
President/CEO
(555)384-9062
www.openhearthfdn.example.org

New Card:
Marcus J. Halvorsen
Director
(555)627-3148
www.openhearthfdn.example.org

New Card:
Norma T. Halvorsen
Director
www.openhearthfdn.example.org

New Card:
Gerald K. Halvorsen
Director
www.openhearthfdn.example.org

Font styles to use
Script

Requirements
Must have
• I want a clean card for all 4 individuals with the logo that was attached.

```html
<!DOCTYPE html>
<html lang="en">
<head>
<meta charset="utf-8">
<title>Wine &amp; Beer Tasting – Colon Cancer Research Fundraiser</title>
<link href="https://fonts.googleapis.com/css2?family=Rye&family=Roboto+Condensed:wght@300;400;700&family=Kaushan+Script&display=swap" rel="stylesheet">
<style>
  :root {
    --page-black: #000000;
    --paper-light: #efe4d2;
    --paper-mid: #e2d2b8;
    --paper-edge: #cdb796;
    --maroon: #5b1d1b;
    --maroon-deep: #4a1512;
    --gold: #b78a3c;
    --gold-light: #c9a056;
    --ink: #4b1a16;
    --ink-soft: #5e3a30;
    --white: #ffffff;
  }
  * { box-sizing: border-box; margin: 0; padding: 0; }
  html, body {
    width: 1200px; height: 900px; overflow: hidden;
    background: var(--page-black);
  }
  .canvas { position: relative; width: 1200px; height: 900px; }
  .flyer {
    position: absolute; left: 285px; top: 0; width: 628px; height: 900px;
    overflow: hidden;
    background: radial-gradient(ellipse at 55% 45%, var(--paper-light) 0%, var(--paper-mid) 60%, var(--paper-edge) 100%);
    font-family: "Roboto Condensed", "Arial Narrow", sans-serif;
    color: var(--ink);
  }
  .abs { position: absolute; }
  .photo { z-index: 0; }
  .text { z-index: 2; }
  .header-band {
    left: 0; top: 27px; width: 628px; height: 53px;
    background: var(--maroon);
    box-shadow: 0 10px 14px -6px rgba(60,30,20,.55);
    display: flex; align-items: center; justify-content: center;
  }
  .header-band span {
    font-family: "Kaushan Script", cursive; color: var(--gold-light);
    font-size: 23px; letter-spacing: .3px;
  }
  .title {
    left: 0; width: 628px; top: 128px; text-align: center;
    font-family: "Rye", serif; font-size: 55px; line-height: 1;
    color: var(--maroon);
    text-shadow: 2px 3px 0 rgba(60,20,15,.35);
    padding-left: 4px;
  }
  .tasting {
    left: 198px; top: 202px; width: 230px; height: 47px;
    border: 1px solid var(--maroon); padding: 3px;
  }
  .tasting span {
    display: flex; width: 100%; height: 100%;
    align-items: center; justify-content: center;
    background: var(--maroon); color: var(--white);
    font-weight: 700; font-size: 27px; letter-spacing: 6px;
  }
  .appetizers {
    left: 0; width: 628px; top: 255px; padding-left: 24px; text-align: center;
    font-family: "Kaushan Script", cursive; color: var(--gold); font-size: 18px;
  }
  .info { left: 172px; width: 300px; text-align: center; }
  .date { top: 313px; font-weight: 700; font-size: 22px; line-height: 1.25; color: var(--ink); }
  .venue { top: 393px; font-weight: 300; font-size: 23px; letter-spacing: 0; color: var(--ink-soft); white-space: nowrap; }
  .address { top: 427px; font-weight: 400; font-size: 14.5px; line-height: 1.35; color: var(--ink-soft); letter-spacing: .5px; }
  .tickets {
    left: 218px; top: 480px; width: 215px; height: 57px;
    background: var(--gold);
    outline: 2px dashed var(--paper-light); outline-offset: -5px;
    display: flex; align-items: center; justify-content: center;
    color: var(--white); font-weight: 700; font-size: 26px;
    text-shadow: 1px 2px 2px rgba(60,30,10,.6);
  }
  .url-band {
    left: 175px; top: 558px; width: 453px; height: 44px;
    background: var(--maroon);
    box-shadow: 0 10px 12px -6px rgba(60,30,20,.5);
    display: flex; align-items: center; padding-left: 32px;
    color: var(--white); font-weight: 700; font-size: 15px; letter-spacing: .3px;
  }
  .contact {
    left: 160px; width: 340px; top: 633px; text-align: center;
    font-weight: 700; font-size: 14px; line-height: 1.25; color: var(--maroon-deep);
  }
  .wine-photo {
    left: 0; top: 195px; width: 175px; height: 565px;
    background: linear-gradient(160deg, #e58ea3 0%, #c21f3a 25%, #8e0f1e 60%, #4e0710 100%);
    border-radius: 80px 70px 90px 90px / 60px 60px 120px 120px;
  }
  .beer-photo {
    left: 470px; top: 205px; width: 158px; height: 675px;
    background: linear-gradient(180deg, #f3eee4 0%, #e8dfcf 14%, #d6a03b 20%, #b87514 55%, #7a4a12 90%, #5a3810 100%);
    border-radius: 14px 0 0 14px;
  }
  .tag {
    height: 31px; background: var(--gold);
    display: flex; align-items: center; justify-content: center;
    font-family: Arial, Helvetica, sans-serif; font-weight: 700; font-size: 14px;
    color: var(--maroon-deep);
    box-shadow: 0 4px 6px rgba(60,30,10,.35);
  }
  .tag-sponsor { left: 35px; top: 744px; width: 170px; }
  .tag-presenter { left: 239px; top: 740px; width: 164px; }
  .sponsor-name {
    left: 45px; top: 799px; display: flex; align-items: center; gap: 8px;
    font-family: "Roboto Condensed", sans-serif; font-size: 15px; color: var(--ink-soft);
  }
  .sponsor-name i { width: 14px; height: 14px; border: 1px solid var(--ink-soft); border-radius: 50%; display: block; }
  .presenter-name {
    left: 239px; top: 790px; display: flex; align-items: center; gap: 9px;
    font-family: "Roboto Condensed", sans-serif; font-weight: 700; font-size: 20px; color: var(--maroon);
  }
  .presenter-name i { width: 30px; height: 30px; background: var(--maroon); border-radius: 50%; display: block; }
</style>
</head>
<body>
<div class="canvas">
  <main class="flyer">
    <div class="abs photo wine-photo" role="img" aria-label="Photo of red wine splashing in a wine glass"></div>
    <div class="abs photo beer-photo" role="img" aria-label="Photo of a frothy glass of golden beer"></div>

    <header class="abs text header-band"><span>Colon Cancer Research Fundraiser</span></header>
    <h1 class="abs text title">WINE &amp; BEER</h1>
    <div class="abs text tasting"><span>TASTING</span></div>
    <p class="abs text appetizers">with appetizers</p>

    <p class="abs text info date">SATURDAY - MAY 9 - 2015<br>5 PM to 8 PM</p>
    <p class="abs text info venue">MAPLECREST RESTAURANT</p>
    <p class="abs text info address">4820 HARBOR VIEW DR<br>CEDAR LAKE, IN 46303</p>

    <div class="abs text tickets">$100 TICKETS</div>
    <div class="abs text url-band">WWW.OPENHEARTHFDN.EXAMPLE.ORG</div>

    <p class="abs text contact">CONTACT: WENDY HALVORSEN 555 - 384 - 9062<br>OR<br>WENDY@OPENHEARTHFDN.EXAMPLE.ORG</p>

    <div class="abs text tag tag-sponsor">SPONSORED BY</div>
    <div class="abs text tag tag-presenter">PRESENTED BY</div>
    <div class="abs text sponsor-name"><i></i>DUNMORE LAW, LLC</div>
    <div class="abs text presenter-name"><i></i>OPEN HEARTH</div>
  </main>
</div>
</body>
</html>
```